Harborline Security and Surveillance Business Card

Business Card Design - Company Name:Freedom Security and SurveillanceWe are a Security Systems Integrator Specializing in Security Systems/ Video Surveillance and Access Control. Our areas of expertise are:Security SystemsVideo SurveillanceAccess ControlFire Alarm SystemsNetwork CablingCellular BoostersMy input is the Front of the Card is: logo, name of Business, My Name, Phone Number, and email.Rear of Card is the 6 areas of expertise, I just dont want the front to be very busy.
Name: Tom Werner
Title: President
Email: tom@harborlinesecsys.example
website: harborlinesecsys.example

```html
<!DOCTYPE html>
<html lang="en">
<head>
<meta charset="utf-8">
<title>Harborline Security and Surveillance – Business Card</title>
<link href="https://fonts.googleapis.com/css2?family=Lato:wght@400;700&display=swap" rel="stylesheet">
<style>
  :root {
    --backdrop: #232323;
    --brand-blue: #0b58b2;
    --brand-blue-soft: #6b9dd1;
    --paper: #ffffff;
    --stripe-grey: #c9ccd0;
    --text-light: #ffffff;
  }
  * { box-sizing: border-box; margin: 0; padding: 0; }
  html, body { width: 1200px; height: 900px; overflow: hidden; }
  body {
    background: var(--backdrop);
    font-family: "Lato", sans-serif;
    position: relative;
  }
  .card {
    position: absolute;
    width: 580px;
    height: 330px;
    overflow: hidden;
    box-shadow: 0 14px 30px rgba(0,0,0,.55);
  }
  /* Front */
  .card--front { left: 90px; top: 80px; background: var(--paper); }
  .front__brand {
    position: absolute; left: 0; right: 0; top: 0; height: 190px;
    display: flex; align-items: center; justify-content: center; gap: 14px;
  }
  .brand__dot {
    width: 26px; height: 26px; border-radius: 50%; background: var(--brand-blue);
  }
  .brand__name {
    color: var(--brand-blue); font-weight: 700; font-size: 23px;
    letter-spacing: 1.5px; text-transform: uppercase; line-height: 1.15;
  }
  .front__stripe {
    position: absolute; left: 0; right: 0; top: 190px; height: 6px; background: var(--stripe-grey);
  }
  .front__band {
    position: absolute; left: 0; right: 0; top: 196px; bottom: 0;
    background: var(--brand-blue); color: var(--text-light);
    display: flex; align-items: center;
  }
  .person {
    width: 310px; text-align: right; padding-right: 26px;
  }
  .person__name { font-weight: 700; font-size: 21px; }
  .person__title { font-size: 11px; letter-spacing: .5px; margin-top: 2px; text-transform: uppercase; }
  .person__address { font-weight: 700; font-size: 13px; margin-top: 14px; }
  .band__divider { width: 2px; height: 86px; background: var(--text-light); }
  .contact { list-style: none; padding-left: 22px; font-size: 13px; }
  .contact li { display: flex; align-items: center; gap: 10px; margin: 6px 0; }
  .contact svg { width: 14px; height: 14px; fill: var(--text-light); }
  /* Back */
  .card--back { left: 530px; top: 490px; background: var(--brand-blue); }
  .back__brand {
    position: absolute; left: 40px; top: 0; bottom: 0; width: 280px;
    display: flex; align-items: center; gap: 16px;
  }
  .back__dot {
    flex: none; width: 40px; height: 40px; border-radius: 50%; background: var(--brand-blue-soft);
  }
  .back__name {
    color: var(--brand-blue-soft); font-weight: 700; font-size: 26px;
    letter-spacing: 1.5px; text-transform: uppercase; line-height: 1.15;
  }
  .services {
    position: absolute; right: 40px; top: 110px;
    list-style: none; text-align: right; color: var(--text-light);
    font-size: 15px; line-height: 1.45;
    border-right: 2px solid var(--text-light); padding-right: 16px;
  }
</style>
</head>
<body>
  <section class="card card--front" aria-label="Card front">
    <div class="front__brand">
      <span class="brand__dot"></span>
      <span class="brand__name">Harborline Security<br>and Surveillance</span>
    </div>
    <div class="front__stripe"></div>
    <div class="front__band">
      <div class="person">
        <p class="person__name">Tom Werner</p>
        <p class="person__title">President</p>
        <p class="person__address">Seefeldweg 14, 8008, Zürich</p>
      </div>
      <div class="band__divider"></div>
      <ul class="contact">
        <li>
          <svg viewBox="0 0 24 24" aria-hidden="true"><path d="M6.6 10.8a15 15 0 0 0 6.6 6.6l2.2-2.2a1 1 0 0 1 1-.25 11 11 0 0 0 3.6.6 1 1 0 0 1 1 1V20a1 1 0 0 1-1 1A17 17 0 0 1 3 4a1 1 0 0 1 1-1h3.5a1 1 0 0 1 1 1 11 11 0 0 0 .6 3.6 1 1 0 0 1-.25 1z"/></svg>
          079 555 01 23
        </li>
        <li>
          <svg viewBox="0 0 24 24" aria-hidden="true"><path d="M2 5h20v14H2z M2 5l10 8 10-8" fill="none" stroke="#fff" stroke-width="2"/></svg>
          tom@harborlinesecsys.example
        </li>
      </ul>
    </div>
  </section>

  <section class="card card--back" aria-label="Card back">
    <div class="back__brand">
      <span class="back__dot"></span>
      <span class="back__name">Harborline Security<br>and Surveillance</span>
    </div>
    <ul class="services">
      <li>Security Systems</li>
      <li>Video Surveillance</li>
      <li>Access Control</li>
      <li>Fire Alarm Systems</li>
      <li>Network Cabling</li>
      <li>Cellular Boosters</li>
    </ul>
  </section>
</body>
</html>
```